Eye catching business card using our brand new logo
Dorvik Fabrication, Inc.
Modern
Wendell R. Fostrey
President
58 Quarry Hollow Road
Brindle, NH 03419
WFostrey@norvax.net
We would like to see many different styles of our brand new logo used in our business cards. Some would fill the card with the logo and some using it in the lower left corner of the card

```html
<!DOCTYPE html>
<html lang="en">
<head>
<meta charset="utf-8">
<title>Dorvik Fabrication, Inc. – Business Card</title>
<link rel="stylesheet" href="https://fonts.googleapis.com/css2?family=Open+Sans:wght@400;600;700&display=swap">
<style>
  :root {
    --page-bg: #e4e5e8;
    --card-bg: #ffffff;
    --card-shade: #f2f2f4;
    --brand-blue: #2f3fc2;
    --brand-blue-dark: #1f2a94;
    --steel: #5b5d63;
    --steel-dark: #2d2e32;
    --text-main: #3a3b40;
    --text-soft: #6b6d73;
  }
  * { margin: 0; padding: 0; box-sizing: border-box; }
  html, body {
    width: 1200px; height: 864px; overflow: hidden;
    background: var(--page-bg);
    font-family: "Open Sans", Arial, sans-serif;
  }
  .sheet {
    position: relative; width: 1200px; height: 864px;
    display: flex; align-items: center; justify-content: center; gap: 50px;
  }
  .card {
    position: relative; width: 540px; height: 312px;
    background: linear-gradient(180deg, var(--card-bg) 0%, var(--card-shade) 100%);
    border-radius: 22px; overflow: hidden;
    box-shadow: 0 10px 28px rgba(0,0,0,.18);
  }
  /* back side */
  .card-back .brand-mark {
    position: absolute; left: 50%; top: 92px; transform: translateX(-50%);
    display: flex; align-items: center; gap: 12px;
  }
  .brand-dot {
    width: 34px; height: 34px; border-radius: 50%; background: var(--steel);
    flex: none;
  }
  .brand-name {
    font-weight: 700; color: var(--brand-blue); white-space: nowrap;
  }
  .card-back .brand-name { font-size: 24px; }
  .card-back .web {
    position: absolute; left: 0; right: 0; top: 196px; text-align: center;
    font-size: 15px; letter-spacing: 5px; color: var(--text-main);
  }
  /* front side */
  .swoosh { position: absolute; left: 0; top: 0; width: 540px; height: 312px; }
  .contact {
    position: absolute; left: 286px; top: 34px; width: 236px;
  }
  .contact .person {
    font-size: 17px; font-weight: 700; color: var(--brand-blue);
  }
  .contact .role {
    font-size: 12px; color: var(--text-soft);
    padding-bottom: 6px; border-bottom: 1px solid #c9cad0; margin-bottom: 10px;
  }
  .contact ul { list-style: none; }
  .contact li {
    display: flex; align-items: center; gap: 8px;
    font-size: 11.5px; color: var(--text-main); height: 19px;
  }
  .contact li .icon { width: 14px; height: 14px; flex: none; }
  .contact li.no-icon { padding-left: 22px; }
  .card-front .brand-mark {
    position: absolute; left: 30px; top: 190px;
    display: flex; align-items: center; gap: 9px;
  }
  .card-front .brand-dot { width: 26px; height: 26px; }
  .card-front .brand-name { font-size: 15px; }
</style>
</head>
<body>
<main class="sheet">

  <section class="card card-back" aria-label="Card back">
    <div class="brand-mark">
      <span class="brand-dot"></span>
      <span class="brand-name">Dorvik Fabrication, Inc.</span>
    </div>
    <p class="web">www.dorvikfab.com</p>
  </section>

  <section class="card card-front" aria-label="Card front">
    <svg class="swoosh" viewBox="0 0 540 312" aria-hidden="true">
      <path d="M0 312 C120 250 300 250 540 176 L540 200 C320 268 150 280 60 312 Z" fill="var(--steel)"/>
      <path d="M120 312 C260 280 420 250 540 190 L540 312 Z" fill="var(--steel-dark)"/>
      <path d="M250 312 C360 282 470 240 540 200 L540 312 Z" fill="var(--brand-blue)"/>
      <path d="M330 312 C420 292 490 262 540 240 L540 312 Z" fill="var(--brand-blue-dark)"/>
    </svg>

    <div class="contact">
      <p class="person">Wendell R. Fostrey</p>
      <p class="role">President</p>
      <ul>
        <li>
          <svg class="icon" viewBox="0 0 14 14" aria-hidden="true"><circle cx="7" cy="7" r="7" fill="var(--brand-blue)"/><path d="M7 3.2a2.3 2.3 0 0 1 2.3 2.3C9.3 7.3 7 10.6 7 10.6S4.7 7.3 4.7 5.5A2.3 2.3 0 0 1 7 3.2z" fill="#fff"/><circle cx="7" cy="5.5" r=".9" fill="var(--brand-blue)"/></svg>
          58 Quarry Hollow Road
        </li>
        <li class="no-icon">Brindle, NH 03419</li>
        <li>
          <svg class="icon" viewBox="0 0 14 14" aria-hidden="true"><circle cx="7" cy="7" r="7" fill="var(--brand-blue)"/><path d="M4.6 3.6l1.3-.3.8 2-.9.7c.4.9 1.1 1.6 2 2l.7-.9 2 .8-.3 1.3c-3 .3-5.9-2.6-5.6-5.6z" fill="#fff"/></svg>
          (603) 555-0142
        </li>
        <li>
          <svg class="icon" viewBox="0 0 14 14" aria-hidden="true"><circle cx="7" cy="7" r="7" fill="var(--brand-blue)"/><rect x="4" y="5.5" width="6" height="4" fill="#fff"/><rect x="5" y="3.6" width="4" height="2" fill="#fff"/></svg>
          (603) 555-0187
        </li>
        <li>
          <svg class="icon" viewBox="0 0 14 14" aria-hidden="true"><circle cx="7" cy="7" r="7" fill="var(--brand-blue)"/><rect x="3.6" y="4.6" width="6.8" height="4.8" fill="#fff"/><path d="M3.6 4.6L7 7.4l3.4-2.8" fill="none" stroke="var(--brand-blue)" stroke-width=".8"/></svg>
          WFostrey@norvax.net
        </li>
      </ul>
    </div>

    <div class="brand-mark">
      <span class="brand-dot"></span>
      <span class="brand-name">Dorvik Fabrication, Inc.</span>
    </div>
  </section>

</main>
</body>
</html>
```